Biz Card for Harrowfield Property Partners - HFPP

Harrowfield Property Partners is a commercial real estate acquisitions firm. We buy commercial property and need to raise capital from investors for each deal we buy. The vibe needs to be: give us your money, we will multiply it.
Our website: www.hfldpp.com
Competitors are: https://marvenby.com/, https://trellumpartners.com/, http://www.quorvantcapital.com/
Target Market(s)
High Net Worth Individuals, Bankers, Insurance Companies, Commercial Real Estate Brokers.
Industry/Entity Type
Investment Banking
Contact Information for Business Card
Name, Title, Addess, Cell#, Office#, email, website
Requirements
Must have
- use one of our logos. See website for look and feel: www.hfldpp.com
Nice to have
- see website: www.hfldpp.com

```html
<!DOCTYPE html>
<html lang="en">
<head>
<meta charset="utf-8">
<title>Harrowfield Property Partners – Business Card</title>
<link rel="stylesheet" href="https://fonts.googleapis.com/css2?family=Roboto:wght@400&display=swap">
<style>
  :root {
    --backdrop: #1f1f20;
    --navy: #0b2340;
    --navy-deep: #07192f;
    --silver: #e6e6e8;
    --silver-shade: #d4d5d8;
    --ink: #0b2340;
    --ink-soft: #2b3d55;
  }
  * { margin: 0; padding: 0; box-sizing: border-box; }
  html, body {
    width: 1200px;
    height: 1138px;
    overflow: hidden;
    background: var(--backdrop);
    font-family: "Roboto", Arial, sans-serif;
  }
  .card {
    position: absolute;
    left: 274px;
    width: 620px;
    height: 374px;
    border-radius: 12px;
    overflow: hidden;
  }
  .card-front {
    top: 186px;
    background: var(--navy);
  }
  .card-back {
    top: 608px;
    background: linear-gradient(135deg, var(--silver), var(--silver-shade));
  }
  .front-emblem {
    position: absolute;
    left: 193px;
    top: 70px;
    width: 236px;
    height: 236px;
    border-radius: 50%;
    background: radial-gradient(circle at 70% 60%, #8f9cac 0%, #3d5068 45%, var(--navy-deep) 85%);
    display: flex;
    align-items: center;
    justify-content: center;
  }
  .brand-mark {
    font-weight: 400;
    letter-spacing: 2px;
  }
  .front-emblem .brand-mark {
    color: var(--navy-deep);
    font-size: 40px;
  }
  .back-panel {
    position: absolute;
    left: 0;
    top: 0;
  }
  .back-emblem {
    position: absolute;
    left: 48px;
    top: 92px;
    width: 184px;
    height: 184px;
    border-radius: 50%;
    background: var(--silver);
    display: flex;
    align-items: center;
    justify-content: center;
  }
  .back-emblem .brand-mark {
    color: var(--navy);
    font-size: 34px;
  }
  .contact-block {
    position: absolute;
    left: 346px;
    top: 84px;
    color: var(--ink);
  }
  .person-name {
    font-size: 24px;
    line-height: 28px;
    color: var(--ink);
  }
  .person-title {
    font-size: 16px;
    line-height: 20px;
    color: var(--ink-soft);
  }
  .contact-list {
    list-style: none;
    margin-top: 20px;
  }
  .contact-list li {
    display: flex;
    align-items: center;
    font-size: 17px;
    line-height: 25px;
    color: var(--ink-soft);
  }
  .contact-list svg {
    width: 14px;
    height: 14px;
    margin-left: 2px;
    margin-right: 12px;
    fill: var(--ink);
  }
  .address {
    font-size: 17px;
    line-height: 25px;
    color: var(--ink-soft);
  }
</style>
</head>
<body>
  <section class="card card-front" aria-label="Card front">
    <div class="front-emblem">
      <span class="brand-mark">HFPP</span>
    </div>
  </section>

  <section class="card card-back" aria-label="Card back">
    <svg class="back-panel" width="620" height="374" viewBox="0 0 620 374">
      <path d="M0 0 H246 Q326 187 246 374 H0 Z" fill="var(--navy)"/>
    </svg>
    <div class="back-emblem">
      <span class="brand-mark">HFPP</span>
    </div>
    <div class="contact-block">
      <p class="person-name">Daniel R. Marsh</p>
      <p class="person-title">Managing Partner</p>
      <ul class="contact-list">
        <li>
          <svg viewBox="0 0 16 16"><path d="M2 6c0-2 2-3.5 6-3.5S14 4 14 6v1h-3V5.5c-1-.4-5-.4-6 0V7H2z M4 8h8l1.5 5.5h-11z"/></svg>
          (305) 418-2960
        </li>
        <li>
          <svg viewBox="0 0 16 16"><path d="M1 3h14v10H1z M2 4.2v.3l6 4.3 6-4.3v-.3z" fill-rule="evenodd"/></svg>
          dmarsh@hfldpp.com
        </li>
        <li>
          <svg viewBox="0 0 16 16"><path fill="none" stroke="var(--ink)" stroke-width="1.4" d="M8 1.5a6.5 6.5 0 1 0 0 13a6.5 6.5 0 1 0 0-13z M1.5 8h13 M8 1.5c-3 3.5-3 9.5 0 13 M8 1.5c3 3.5 3 9.5 0 13"/></svg>
          www.hfldpp.com
        </li>
      </ul>
      <p class="address">455 Meridian Ave, Suite 810</p>
      <p class="address">Coral Gables, FL 33146</p>
    </div>
  </section>
</body>
</html>
```